VALMIK GROUP

This is a company that provides executive protection. Our motto is "New Era in Protection"... I don't want this to look like other security websites. I want it to be clean and sharp and represent a new era. We are based in the bay area so maybe a picture of San Francisco in the background?
I want it to be able to funnel down a couple different categories.
1. About Us
2. Services (Executive Protection, Covert Protection, Residential Protection & Intelligence)
3. Blue Pike (Training & Consulting)
4. Contact Us
I want it to be very clean and modern. I don't want there to be any pictures of bodyguards with ear pieces like every other website.
Target Market(s)
Ultra High Net Worth Individuals
Coding
Coded - Design and coding required
Number of Pages Required
1 page
Requirements
Must have
- Colors of my Symbol
Nice to have
- City in the background, San Francisco, New York or the Thornmeadow Club in Montana.
Should not have
- Should not look like an KVM website or have photos of bodyguards. I want this to be a clean and simple website with my logo

```html
<!DOCTYPE html>
<html lang="en">
<head>
<meta charset="utf-8">
<title>Valmik Group — New Era in Protection</title>
<link href="https://fonts.googleapis.com/css2?family=Ubuntu:wght@300;400;500;700&family=Lato:wght@300;400;700&display=swap" rel="stylesheet">
<style>
:root{
  --red:#8e1a1f;
  --red-deep:#6e0f13;
  --navy:#0c1a4f;
  --ink:#1b1b1b;
  --text:#7a7a7a;
  --line:#ececec;
  --footer:#1c1c1e;
  --white:#ffffff;
}
*{box-sizing:border-box;margin:0;padding:0}
html,body{width:1200px;height:4129px;overflow:hidden;background:var(--white)}
body{position:relative;font-family:"Lato",sans-serif;color:var(--text)}
section,header,footer{position:absolute;left:0;width:1200px}
.abs{position:absolute}
.guides{position:absolute;inset:0;pointer-events:none;z-index:5}
.guides span{position:absolute;top:0;bottom:0;width:1px;background:rgba(200,200,200,.28)}
.btn{position:absolute;height:32px;border-radius:16px;background:var(--red);color:var(--white);font:700 13px "Lato",sans-serif;display:flex;align-items:center;justify-content:center;letter-spacing:.2px}
.heading{font:700 35px "Ubuntu",sans-serif;color:var(--ink);letter-spacing:-.3px}

/* header */
.site-header{top:0;height:109px;background:var(--white);z-index:6}
.brand{left:157px;top:36px;font:700 20px "Ubuntu",sans-serif;color:var(--red);display:flex;align-items:center;gap:8px}
.brand i{width:14px;height:14px;background:var(--red);display:block}
.topbar{left:689px;top:0;width:511px;height:40px;background:var(--red);clip-path:polygon(0 0,100% 0,100% 100%,22px 100%);color:var(--white);font-size:13px}
.topbar .item{position:absolute;top:10px;display:flex;align-items:center;gap:9px}
.topbar .dot{width:24px;height:24px;border-radius:50%;background:var(--white);display:flex;align-items:center;justify-content:center}
.nav a{position:absolute;top:69px;font-size:13px;color:#8b8b8b;text-decoration:none}
.nav a.active{color:var(--ink)}
.nav a.active::after{content:"";position:absolute;left:0;right:0;bottom:-9px;height:2px;background:var(--red)}

/* hero */
.hero{top:109px;height:529px;background:linear-gradient(180deg,#1d2433 0%,#2c3850 38%,#5a4a3a 62%,#2a2420 100%);text-align:center;color:var(--white)}
.hero .t1{top:135px;width:100%;font:300 48px "Ubuntu",sans-serif}
.hero .t2{top:183px;width:100%;font:400 80px "Ubuntu",sans-serif;line-height:1}
.hero .sub{top:290px;width:100%;font:300 26px "Ubuntu",sans-serif}
.hero .dots{top:448px;left:580px;display:flex;gap:8px;align-items:center}
.hero .dots b{width:4px;height:4px;background:var(--white);display:block}
.hero .dots b.on{width:7px;height:7px}

/* about */
.about{top:638px;height:491px}
.about p{left:607px;top:160px;width:432px;font-size:13.5px;line-height:25.6px}

/* services */
.services{top:1129px;height:670px;background:linear-gradient(100deg,#081a55 0%,#1a2563 45%,#55204a 70%,#8d1a22 100%);color:var(--white)}
.services .heading{color:var(--white);width:100%;text-align:center;top:82px}
.svc h3{position:absolute;font:500 20px "Ubuntu",sans-serif;line-height:26px}
.svc p{position:absolute;font-size:13.5px;line-height:23px;width:280px;color:#e6e6ee}
.svc.left h3,.svc.left p{right:756px;text-align:right}
.svc.right h3,.svc.right p{left:756px}

/* blue pike */
.bluepike{top:1799px;height:1029px}
.bluepike .heading{width:100%;text-align:center;top:88px}
.blob{position:absolute;background:var(--red);border-radius:50%}
.photo{position:absolute;border:2px solid #fff;box-shadow:0 0 0 1px #ddd;border-radius:6px 40px 6px 40px}
.bluepike h3{position:absolute;font:300 27px "Ubuntu",sans-serif;color:var(--ink)}
.bluepike p{position:absolute;width:370px;font-size:13.5px;line-height:25.6px}

/* contact */
.contact{top:2828px;height:514px}
.contact .heading{color:var(--white);left:607px;top:132px}
.field{position:absolute;border:1px solid rgba(255,255,255,.75);color:var(--white);font-size:12.5px;padding:12px 13px}
.btn.light{background:var(--white);color:var(--red)}

/* newsletter */
.newsletter{top:3342px;height:331px}
.newsletter .heading{width:100%;text-align:center;top:78px}
.mail{left:314px;top:150px;width:572px;height:52px;border:1px solid #d8d8d8;box-shadow:0 2px 6px rgba(0,0,0,.08);display:flex;align-items:center;justify-content:center;font-size:13px;color:var(--ink)}

/* footer */
.site-footer{top:3673px;height:456px;background:linear-gradient(180deg,#242428 0%,#17171a 100%);color:#cfcfcf}
.site-footer h4{position:absolute;top:122px;font:400 17px "Ubuntu",sans-serif;color:#e8e8e8}
.site-footer ul{position:absolute;top:166px;list-style:none;font-size:13px;line-height:25.6px}
.site-footer .about-text{position:absolute;left:157px;top:166px;width:290px;font-size:13px;line-height:23.5px}
.site-footer li{display:flex;align-items:center;gap:12px}
.social{left:521px;top:334px;display:flex;gap:7px}
.social span{width:34px;height:34px;border-radius:50%;background:var(--white);display:block}
.copy{top:390px;width:100%;text-align:center;font-size:11.5px;color:#aaa}
</style>
</head>
<body>

<header class="site-header">
  <div class="abs brand"><i></i>VALMIK GROUP</div>
  <div class="abs topbar">
    <div class="item" style="left:40px"><span class="dot"><svg width="12" height="14" viewBox="0 0 12 14"><path d="M6 0a5 5 0 0 0-5 5c0 4 5 9 5 9s5-5 5-9a5 5 0 0 0-5-5zm0 7a2 2 0 1 1 0-4 2 2 0 0 1 0 4z" fill="#8e1a1f"/></svg></span>lorem Ipsum, New york</div>
    <div class="item" style="left:245px"><span class="dot"><svg width="13" height="13" viewBox="0 0 24 24"><path d="M6.6 10.8a15 15 0 0 0 6.6 6.6l2.2-2.2a1 1 0 0 1 1-.25 11 11 0 0 0 3.6.6 1 1 0 0 1 1 1V20a1 1 0 0 1-1 1A17 17 0 0 1 3 4a1 1 0 0 1 1-1h3.5a1 1 0 0 1 1 1 11 11 0 0 0 .6 3.6 1 1 0 0 1-.25 1z" fill="#8e1a1f"/></svg></span>555-010-274</div>
  </div>
  <nav class="nav">
    <a class="active" href="#" style="left:610px">Home</a>
    <a href="#" style="left:697px">About</a>
    <a href="#" style="left:782px">Services</a>
    <a href="#" style="left:881px">Blue Pike</a>
    <a href="#" style="left:977px">Contact Us</a>
  </nav>
</header>

<section class="hero" role="img" aria-label="Night city skyline with a lit suspension bridge over the water">
  <div class="abs t1">New Era in</div>
  <div class="abs t2">Protection</div>
  <div class="abs sub">It is a long established fact that reader will be distracted</div>
  <div class="btn" style="left:543px;top:351px;width:112px">READ MORE</div>
  <div class="abs dots"><b></b><b class="on"></b><b></b></div>
</section>

<section class="about">
  <svg class="abs" style="left:157px;top:77px" width="336" height="358" viewBox="0 0 336 358" role="img" aria-label="Hand holding a glowing digital security lock">
    <defs><linearGradient id="aboutFill" x1="0" y1="0" x2="1" y2="1"><stop offset="0" stop-color="#5f8fa0"/><stop offset=".5" stop-color="#b9c7c9"/><stop offset="1" stop-color="#c56a3c"/></linearGradient></defs>
    <polygon points="0,0 336,0 336,253 168,358 0,253" fill="url(#aboutFill)"/>
  </svg>
  <h2 class="abs heading" style="left:610px;top:112px">ABOUT US</h2>
  <p class="abs">Many desktop publishing packages and web page editors now use Lorem Ipsum as their default model text, and a search for 'lorem ipsum' will uncover many web sites still in their infancy. Various versions have evolved over the years, sometimes by accident,It is a long established fact that a reader will be distracted by the readable content of a page when looking at its layout.</p>
  <div class="btn" style="left:607px;top:336px;width:115px">READ MORE</div>
</section>

<section class="services">
  <h2 class="abs heading">OUR SERVICES</h2>
  <svg class="abs" style="left:455px;top:170px" width="290" height="372" viewBox="0 0 290 372">
    <g stroke="#fff" stroke-width="8">
      <polygon points="72,4 140,42 140,116 72,154 4,116 4,42" fill="#9aa7c4" role="img" aria-label="Hand touching a digital lock icon"/>
      <polygon points="219,4 287,42 287,116 219,154 151,116 151,42" fill="#8f8579" role="img" aria-label="Security camera mounted on a wall"/>
      <polygon points="72,220 140,258 140,332 72,370 4,332 4,258" fill="#6f7f66" role="img" aria-label="Outdoor surveillance camera"/>
      <polygon points="219,220 287,258 287,332 219,370 151,332 151,258" fill="#c9a585" role="img" aria-label="Hands typing on a laptop"/>
    </g>
  </svg>
  <div class="svc left"><h3 style="top:190px">Executive<br>Protection</h3><p style="top:263px">Many desktop publishing packages and web page editors now use Lorem Ipsum as their default model text</p></div>
  <div class="svc right"><h3 style="top:190px">Residential<br>Protection</h3><p style="top:263px">Many desktop publishing packages and web page editors now use Lorem Ipsum as their default model text</p></div>
  <div class="svc left"><h3 style="top:408px">Covert<br>Protection</h3><p style="top:481px">Many desktop publishing packages and web page editors now use Lorem Ipsum as their default model text</p></div>
  <div class="svc right"><h3 style="top:409px">Intelligence</h3><p style="top:446px">Many desktop publishing packages and web page editors now use Lorem Ipsum as their default model text</p></div>
</section>

<section class="bluepike">
  <h2 class="abs heading">BLUE PIKE</h2>
  <div class="blob" style="left:159px;top:284px;width:434px;height:304px;border-radius:45% 45% 50% 50%/30% 30% 70% 70%"></div>
  <div class="photo" style="left:221px;top:175px;width:327px;height:381px;background:linear-gradient(160deg,#dfe9ea,#b8c9c9 55%,#a4685a)" role="img" aria-label="Trainer presenting to a seated group"></div>
  <h3 style="left:662px;top:284px">Training</h3>
  <p style="left:666px;top:338px">Many desktop publishing packages and web page editors now use Lorem Ipsum as their default model text, and a search for 'lorem ipsum' will uncover many web sites still in their infancy. Various versions have evolved over</p>
  <h3 style="left:159px;top:674px">Consulting</h3>
  <p style="left:156px;top:728px">Many desktop publishing packages and web page editors now use Lorem Ipsum as their default model text, and a search for 'lorem ipsum' will uncover many web sites still in their infancy. Various versions have evolved over</p>
  <div class="blob" style="left:607px;top:668px;width:434px;height:308px;border-radius:45% 45% 50% 50%/30% 30% 70% 70%"></div>
  <div class="photo" style="left:670px;top:562px;width:326px;height:378px;background:linear-gradient(160deg,#e6e9ec,#4a5b78 55%,#cfd3d6)" role="img" aria-label="Two consultants in suits reviewing documents at a laptop"></div>
</section>

<section class="contact">
  <svg class="abs" style="left:0;top:0" width="1200" height="514" viewBox="0 0 1200 514">
    <defs><linearGradient id="wave" x1="0" y1="0" x2="1" y2="1"><stop offset="0" stop-color="#5c0c10"/><stop offset=".6" stop-color="#8a171c"/><stop offset="1" stop-color="#7a1217"/></linearGradient></defs>
    <path d="M0 63 C180 130 300 200 520 150 C760 96 900 -8 1050 0 C1130 4 1170 22 1200 40 V514 H0 Z" fill="url(#wave)"/>
  </svg>
  <div class="abs" style="left:157px;top:8px;width:380px;height:506px;border-radius:190px 190px 0 0;background:linear-gradient(180deg,#6b5a50 0%,#7d7c80 45%,#4e4e54 100%)" role="img" aria-label="Smiling man in a grey suit holding a phone"></div>
  <h2 class="abs heading">CONTACT US</h2>
  <div class="field" style="left:607px;top:193px;width:212px;height:44px">First Name :</div>
  <div class="field" style="left:831px;top:193px;width:212px;height:44px">Last Name :</div>
  <div class="field" style="left:607px;top:248px;width:212px;height:43px">Phone No :</div>
  <div class="field" style="left:831px;top:248px;width:212px;height:43px">Email :</div>
  <div class="field" style="left:607px;top:305px;width:436px;height:105px">Message :</div>
  <div class="btn light" style="left:607px;top:418px;width:114px;height:30px">SUBMIT NOW</div>
</section>

<section class="newsletter">
  <h2 class="abs heading">NEWSLETTER</h2>
  <div class="abs mail">Enter Your Mail ID</div>
  <div class="btn" style="left:522px;top:219px;width:156px">SUBSCRIBE NOW</div>
</section>

<footer class="site-footer" role="img" aria-label="Faint night city skyline behind the footer">
  <h4 style="left:157px">About</h4>
  <p class="about-text">All the Lorem Ipsum generators on the Internet tend to repeat predefined chunks as necessary, making this the first true generator on the Internet. It uses a dictionary .All the Lorem Ipsum generators on the Internet tend .</p>
  <h4 style="left:530px">Services</h4>
  <ul style="left:530px"><li>Executive Protection</li><li>Covert Protection</li><li>Residential Protection</li><li>Intelligence</li></ul>
  <h4 style="left:726px">Quick Link</h4>
  <ul style="left:726px"><li>Home</li><li>About</li><li>Services</li><li>Blue Pike</li><li>Contact Us</li></ul>
  <h4 style="left:878px">Contact Us</h4>
  <ul style="left:878px">
    <li><svg width="9" height="11" viewBox="0 0 12 14"><path d="M6 0a5 5 0 0 0-5 5c0 4 5 9 5 9s5-5 5-9a5 5 0 0 0-5-5z" fill="#fff"/></svg>loremipsum,New York</li>
    <li><svg width="9" height="9" viewBox="0 0 24 24"><path d="M6.6 10.8a15 15 0 0 0 6.6 6.6l2.2-2.2a1 1 0 0 1 1-.25 11 11 0 0 0 3.6.6 1 1 0 0 1 1 1V20a1 1 0 0 1-1 1A17 17 0 0 1 3 4a1 1 0 0 1 1-1h3.5a1 1 0 0 1 1 1 11 11 0 0 0 .6 3.6 1 1 0 0 1-.25 1z" fill="#fff"/></svg>555-010-274</li>
    <li><svg width="9" height="8" viewBox="0 0 10 8"><rect width="10" height="8" fill="#fff"/><path d="M0 0l5 4 5-4" stroke="#1c1c1e" fill="none"/></svg>hello@valmikgroup.test</li>
  </ul>
  <div class="abs social"><span></span><span></span><span></span><span></span></div>
  <div class="abs copy">Copyright © 2021 <span style="color:#fff">Valmik</span> - All rights reserved.</div>
</footer>

<div class="guides"><span style="left:224px"></span><span style="left:476px"></span><span style="left:726px"></span><span style="left:976px"></span></div>
</body>
</html>
```